Business Card Design

I would like a logo created for the top left corner of the card please. I would like a checkerboard in a dark navy with the edges fading out and one random bright orange square.
Updates

I have attached some further notes and a really rough sketch of what I am after.  Thank you. :)

Target Market(s)

Construction, mining, mechanical

Industry/Entity Type

Business

Contact Information for Business Card

KRW Fabrications Pty Ltd, Oscar Plunkett, P. 0413658207, F. 0753917260, E.oscar@krwfabrications.com.au, PO Box 87 WONGARA Q 4571, ABN 52983470611

Font styles to use
Sans Serif

Requirements
Must have
• Really Dark Navy
Really bright Orange

```html
<!DOCTYPE html>
<html lang="en">
<head>
<meta charset="utf-8">
<title>KRW Fabrications Business Card</title>
<link rel="stylesheet" href="https://fonts.googleapis.com/css2?family=Alfa+Slab+One&family=Open+Sans:wght@400&display=swap">
<style>
  :root {
    --navy: #23246b;
    --orange: #ea7a1f;
    --orange-deep: #d9661a;
    --white: #ffffff;
    --paper: #f2f2f2;
    --backdrop: #2b2b2b;
  }
  * { margin: 0; padding: 0; box-sizing: border-box; }
  html, body {
    width: 1200px;
    height: 900px;
    overflow: hidden;
    background: var(--backdrop);
  }
  .card {
    position: absolute;
    left: 100px;
    top: 145px;
    width: 1000px;
    height: 611px;
    overflow: hidden;
    box-shadow: 0 12px 40px rgba(0, 0, 0, 0.5);
  }
  .card-bands {
    position: absolute;
    inset: 0;
    width: 100%;
    height: 100%;
  }
  .brand {
    position: absolute;
    left: 60px;
    top: 118px;
    display: flex;
    align-items: center;
    gap: 22px;
    white-space: nowrap;
  }
  .brand-mark {
    width: 46px;
    height: 46px;
    background: var(--orange);
  }
  .brand-name {
    font-family: "Alfa Slab One", serif;
    font-size: 44px;
    line-height: 1;
    color: var(--navy);
    letter-spacing: 0.5px;
  }
  .holder-name {
    position: absolute;
    left: 60px;
    top: 282px;
    font-family: "Alfa Slab One", serif;
    font-size: 46px;
    font-weight: 400;
    line-height: 1;
    color: var(--navy);
    white-space: nowrap;
  }
  .holder-name .first { color: var(--paper); }
  .contact-list {
    position: absolute;
    left: 60px;
    top: 372px;
    list-style: none;
    font-family: "Open Sans", sans-serif;
    font-size: 30px;
    color: var(--paper);
  }
  .contact-list li {
    display: flex;
    align-items: center;
    gap: 20px;
    height: 66px;
    white-space: nowrap;
  }
  .contact-icon {
    width: 34px;
    height: 34px;
    flex: none;
  }
  .company-details {
    position: absolute;
    left: 580px;
    top: 240px;
    font-family: "Open Sans", sans-serif;
    font-size: 24px;
    color: var(--paper);
  }
  .company-details p {
    display: flex;
    align-items: center;
    gap: 14px;
    height: 44px;
    white-space: nowrap;
  }
  .company-details .contact-icon {
    width: 30px;
    height: 30px;
  }
  .abn-label { color: var(--navy); }
</style>
</head>
<body>
  <article class="card">
    <svg class="card-bands" viewBox="0 0 1000 611" preserveAspectRatio="none" aria-hidden="true">
      <defs>
        <linearGradient id="orangeFill" x1="0" y1="0" x2="1" y2="1">
          <stop offset="0" stop-color="#ee8428"/>
          <stop offset="1" stop-color="#d9661a"/>
        </linearGradient>
      </defs>
      <rect width="1000" height="611" fill="url(#orangeFill)"/>
      <polygon points="0,0 1000,0 1000,160 0,238" fill="#ffffff"/>
      <polygon points="0,238 1000,160 1000,170 0,248" fill="#23246b"/>
    </svg>

    <div class="brand">
      <span class="brand-mark"></span>
      <span class="brand-name">KRW Fabrications Pty Ltd</span>
    </div>

    <h1 class="holder-name"><span class="first">Oscar</span> Plunkett</h1>

    <ul class="contact-list">
      <li>
        <svg class="contact-icon" viewBox="0 0 24 24" aria-label="Phone">
          <path fill="#23246b" d="M6.6 10.8a15.1 15.1 0 0 0 6.6 6.6l2.2-2.2a1 1 0 0 1 1-.25 11.4 11.4 0 0 0 3.6.57 1 1 0 0 1 1 1V20a1 1 0 0 1-1 1A17 17 0 0 1 3 4a1 1 0 0 1 1-1h3.5a1 1 0 0 1 1 1c0 1.25.2 2.45.57 3.57a1 1 0 0 1-.25 1z"/>
        </svg>
        0413658207
      </li>
      <li>
        <svg class="contact-icon" viewBox="0 0 24 24" aria-label="Fax">
          <g fill="none" stroke="#23246b" stroke-width="1.8">
            <rect x="3" y="10" width="18" height="10" rx="1"/>
            <path d="M7 10V4h8l2 2v4"/>
            <path d="M7 14h4M7 17h4"/>
          </g>
          <rect x="14" y="13" width="4" height="4" fill="#23246b"/>
        </svg>
        0753917260
      </li>
      <li>
        <svg class="contact-icon" viewBox="0 0 24 24" aria-label="Email">
          <text x="12" y="19" text-anchor="middle" font-family="Open Sans, sans-serif" font-size="22" fill="#23246b">@</text>
        </svg>
        oscar@krwfabrications.com.au
      </li>
    </ul>

    <div class="company-details">
      <p>
        <svg class="contact-icon" viewBox="0 0 24 24" aria-label="Postal address">
          <g fill="none" stroke="#23246b" stroke-width="1.6">
            <rect x="2" y="5" width="20" height="14"/>
            <path d="M2 5l10 8 10-8"/>
          </g>
        </svg>
        PO Box 87 WONGARA Q 4571
      </p>
      <p><span class="abn-label">ABN</span> 52983470611</p>
    </div>
  </article>
</body>
</html>
```